Wine Label: Corvinte

The project is to create 3 wine labels. The brand name is "Corvinte"

What we need is to have 3 versions: red wine, white wine and rose.

The wine is for young and modern people, between 21 and 31 years old, so it need to be casual, modern and fun, but at the same time it needs to keep the Premiums of a good European wine.

It is from Italy.

Target Market(s)

Young adults, between 21 and 31 years old. wine lovers

Requirements
Must have
• - Modern colors (Black, silver, red, etc.)
• - Clean label
• - Clear font
• - Style
• - The brand + the type of wine (red, white or rose)
Nice to have
• - A symbol to represent the brand
Should not have
• - Many elements
• - No clear fonts
• - No funny colors

```html
<!DOCTYPE html>
<html lang="en">
<head>
<meta charset="utf-8">
<title>Corvinte Wine Labels</title>
<link rel="stylesheet" href="https://fonts.googleapis.com/css2?family=Marcellus&family=Montserrat:wght@400;500&display=swap">
<style>
  :root {
    --page: #ffffff;
    --ink-light: #ffffff;
    --white-glass-top: #d9dab0;
    --white-glass-bottom: #a9ac74;
    --rose-glass-top: #ef9a8e;
    --rose-glass-bottom: #de6a63;
    --red-glass-top: #2a1c1e;
    --red-glass-bottom: #120c0d;
    --white-art-a: #f7f3d6;
    --white-art-b: #e9e3b4;
    --rose-art-a: #f6dfec;
    --rose-art-b: #d84f98;
    --red-art-a: #e79ac0;
    --red-art-b: #e0304f;
  }
  * { margin: 0; padding: 0; box-sizing: border-box; }
  html, body { width: 1200px; height: 1148px; overflow: hidden; background: var(--page); }
  .canvas {
    position: relative;
    width: 1200px;
    height: 1148px;
    background: var(--page);
    overflow: hidden;
  }
  .label {
    position: absolute;
    top: 200px;
    width: 300px;
    height: 740px;
    overflow: hidden;
    color: var(--ink-light);
    text-align: center;
  }
  .label--white { left: 90px;  background: linear-gradient(180deg, var(--white-glass-top), var(--white-glass-bottom)); }
  .label--rose  { left: 450px; background: linear-gradient(180deg, var(--rose-glass-top), var(--rose-glass-bottom)); }
  .label--red   { left: 810px; background: linear-gradient(180deg, var(--red-glass-top), var(--red-glass-bottom)); }

  .brand {
    position: absolute;
    top: 96px;
    left: 0;
    width: 100%;
    font-family: "Marcellus", serif;
    font-weight: 400;
    font-size: 44px;
    letter-spacing: 0.1em;
    line-height: 1;
  }
  .variety {
    position: absolute;
    top: 150px;
    left: 0;
    width: 100%;
    font-family: "Montserrat", sans-serif;
    font-weight: 400;
    font-size: 10px;
    letter-spacing: 0.3em;
    line-height: 1;
    color: var(--ink-light);
  }
  .hand-art {
    position: absolute;
    top: 240px;
    left: 0;
    width: 250px;
    height: 300px;
    clip-path: polygon(0 42%, 30% 30%, 48% 2%, 70% 0, 92% 8%, 100% 30%, 88% 52%, 60% 72%, 30% 100%, 0 100%);
  }
  .label--white .hand-art { background: linear-gradient(135deg, var(--white-art-a), var(--white-art-b)); }
  .label--rose  .hand-art { background: linear-gradient(135deg, var(--rose-art-a), var(--rose-art-b)); }
  .label--red   .hand-art { background: linear-gradient(135deg, var(--red-art-a), var(--red-art-b)); }

  .winery {
    position: absolute;
    top: 574px;
    left: 0;
    width: 100%;
    font-family: "Marcellus", serif;
    font-size: 17px;
    letter-spacing: 0.2em;
    line-height: 1;
  }
  .tagline {
    position: absolute;
    top: 612px;
    left: 0;
    width: 100%;
    font-family: "Montserrat", sans-serif;
    font-weight: 400;
    font-size: 7px;
    letter-spacing: 0.15em;
    line-height: 1.5;
    text-transform: uppercase;
  }
</style>
</head>
<body>
<main class="canvas">
  <section class="label label--white">
    <h2 class="brand">CORVINTE</h2>
    <p class="variety">WHITE</p>
    <div class="hand-art" role="img" aria-label="Watercolour illustration of two reaching hands in pale cream tones"></div>
    <p class="winery">WINERY NAME</p>
    <p class="tagline">Something clever<br>Wine of Italy</p>
  </section>

  <section class="label label--rose">
    <h2 class="brand">CORVINTE</h2>
    <p class="variety">ROSE</p>
    <div class="hand-art" role="img" aria-label="Watercolour illustration of two reaching hands in pink and magenta tones"></div>
    <p class="winery">WINERY NAME</p>
    <p class="tagline">Something clever<br>Wine of Italy</p>
  </section>

  <section class="label label--red">
    <h2 class="brand">CORVINTE</h2>
    <p class="variety">RED</p>
    <div class="hand-art" role="img" aria-label="Watercolour illustration of two reaching hands in pink and red tones"></div>
    <p class="winery">WINERY NAME</p>
    <p class="tagline">Something clever<br>Wine of Italy</p>
  </section>
</main>
</body>
</html>
```